Design a New Business Card for Our Company

We are looking for fresh, unique, and a modern business card that reflects our roots as digital marketing agency focused on SEM.

Industry/Entity Type

Marketing

Contact Information for Business Card

looking for very unique out of the box designs. clean and modern that compliments our logo

Requirements
Must have
• colors should match our logo
• Front should have name, address, email, and phone/fax of the person, phone/fax are the same number
• back should have our url

```html
<!DOCTYPE html>
<html lang="en">
<head>
<meta charset="utf-8">
<title>Northgate Media – Business Card</title>
<link rel="stylesheet" href="https://fonts.googleapis.com/css2?family=Arimo:wght@400;700&display=swap">
<style>
  :root {
    --backdrop: #3b3431;
    --card: #1b1b1d;
    --card-edge: #29292c;
    --brand-blue: #4a8fd6;
    --brand-grey: #b9babd;
    --text-light: #e6e6e8;
    --text-muted: #9a9ba0;
    --divider: #55565b;
  }
  * { box-sizing: border-box; margin: 0; padding: 0; }
  html, body {
    width: 1200px; height: 787px; overflow: hidden;
    background: var(--backdrop);
    font-family: "Arimo", Arial, sans-serif;
  }
  .canvas {
    position: relative; width: 1200px; height: 787px;
    display: flex; align-items: center; justify-content: center; gap: 60px;
  }
  .card {
    position: relative; width: 520px; height: 298px;
    background: var(--card);
    border: 1px solid var(--card-edge);
    box-shadow: 0 14px 30px rgba(0,0,0,.45);
    color: var(--text-light);
  }
  /* back side */
  .card-back { display: flex; flex-direction: column; align-items: center; justify-content: center; }
  .back-mark { width: 92px; height: 92px; border-radius: 50%; background: var(--brand-blue); margin-bottom: 28px; }
  .back-url {
    position: absolute; left: 42px; bottom: 46px;
    font-size: 13px; letter-spacing: 5px; color: var(--text-light);
  }
  /* front side */
  .brand {
    position: absolute; top: 62px; right: 48px;
    display: flex; align-items: center; gap: 12px;
  }
  .brand-dot { width: 30px; height: 30px; border-radius: 50%; background: var(--brand-blue); }
  .brand-name { font-size: 40px; font-weight: 700; color: var(--brand-grey); letter-spacing: -0.5px; }
  .person {
    position: absolute; top: 178px; right: 300px; text-align: right;
  }
  .person-name { font-size: 18px; font-weight: 700; color: var(--brand-grey); }
  .person-title { font-size: 15px; color: var(--brand-blue); margin-top: 4px; }
  .divider {
    position: absolute; left: 236px; top: 170px; width: 1px; height: 96px;
    background: linear-gradient(var(--divider), transparent);
  }
  .contact {
    position: absolute; left: 256px; top: 172px;
    font-size: 15px; line-height: 19px; color: var(--text-light);
    list-style: none;
  }
  .contact li { display: flex; align-items: center; gap: 9px; }
  .contact .address { padding-left: 23px; }
  .contact svg { width: 14px; height: 14px; fill: var(--text-muted); flex: none; }
</style>
</head>
<body>
<main class="canvas">
  <section class="card card-back" aria-label="Card back">
    <div class="back-mark"></div>
    <p class="back-url">www.ngmedia.com</p>
  </section>

  <section class="card card-front" aria-label="Card front">
    <div class="brand">
      <span class="brand-dot"></span>
      <span class="brand-name">Northgate Media</span>
    </div>

    <div class="person">
      <p class="person-name">Marcus Hale</p>
      <p class="person-title">President</p>
    </div>

    <div class="divider"></div>

    <ul class="contact">
      <li class="address">2190 Alder Grove Road</li>
      <li class="address">Millbrook, NY 12545</li>
      <li>
        <svg viewBox="0 0 16 16" aria-hidden="true"><path d="M3.6 1.2l2.4 2.6-1.3 2a8.5 8.5 0 0 0 5.5 5.5l2-1.3 2.6 2.4-1.6 2.3C7 14.4 1.6 9 1.3 2.8z"/></svg>
        555 0142 7781
      </li>
      <li>
        <svg viewBox="0 0 16 16" aria-hidden="true"><path d="M4 1h7l1 1v3H4zM2 6h12a1 1 0 0 1 1 1v5h-3v3H4v-3H1V7a1 1 0 0 1 1-1zm3 5v3h6v-3z"/></svg>
        555 0198 3460
      </li>
      <li>
        <svg viewBox="0 0 16 16" aria-hidden="true"><path d="M1 3h14v10H1zm1.5 1.2V5l5.5 4 5.5-4v-.8z"/></svg>
        marcus@ngmedia.com
      </li>
    </ul>
  </section>
</main>
</body>
</html>
```